Business Card Design Project

We are not a new company, but renamed to "Norvanta Kitchens" last year. We specialize in modern high-end cabinetry imports. We would like to communicate a sense of quality and cutting edge technology. Ideally the design would incorporate our logo colors, silver, red and preferably a black, matte background. Though we are open to suggestions.
Logo is attached.
Edit: I have attached rough drafts of the previous cards, this way you will have all necessary content that needs to go on the cards.
Reason: We have received a lot of great designs, but due to the sheer number we couldn't respond to all. We will extend the deadline for another 7 days to finalize and provide feedback to designers.
Thank you for your hard work!
Industry/Entity Type
Business
Look and feel
Each slider illustrates characteristics of the customer's brand and the style your logo design should communicate.

```html
<!DOCTYPE html>
<html lang="en">
<head>
<meta charset="utf-8">
<title>Norvanta Kitchens — Business Card</title>
<link rel="stylesheet" href="https://fonts.googleapis.com/css2?family=Saira:wght@400;500;600&display=swap">
<style>
  :root {
    --backdrop: #3b3532;
    --card-black: #141414;
    --card-edge: #1d1d1d;
    --silver: #c9c9c9;
    --silver-soft: #a9a9a9;
    --red: #c8141e;
  }
  * { margin: 0; padding: 0; box-sizing: border-box; }
  html, body { width: 1200px; height: 716px; overflow: hidden; }
  body {
    background: var(--backdrop);
    font-family: "Saira", "Helvetica Neue", Arial, sans-serif;
    position: relative;
  }
  .card {
    position: absolute;
    top: 215px;
    width: 500px;
    height: 286px;
    background: linear-gradient(160deg, var(--card-edge), var(--card-black) 60%);
    border-radius: 4px;
    box-shadow: 0 12px 30px rgba(0,0,0,.45);
    color: var(--silver);
  }
  .card--front { left: 60px; }
  .card--back { left: 640px; }

  .brand-name {
    font-weight: 600;
    text-transform: uppercase;
    color: var(--silver);
    letter-spacing: .04em;
    display: flex;
    align-items: center;
    gap: 12px;
  }
  .brand-mark {
    width: 14px; height: 14px;
    background: var(--silver);
    flex: none;
  }
  .card--front .brand-name {
    position: absolute;
    top: 100px; left: 0; right: 0;
    justify-content: center;
    font-size: 34px;
  }
  .web {
    position: absolute;
    color: var(--red);
    font-size: 15px;
    letter-spacing: .12em;
  }
  .card--front .web { left: 40px; bottom: 30px; }
  .card--back .web { right: 34px; bottom: 26px; }

  .card--back .brand-name {
    position: absolute;
    top: 40px; right: 40px;
    font-size: 26px;
  }
  .person {
    position: absolute;
    top: 96px; left: 40px;
    font-size: 19px;
    letter-spacing: .02em;
    text-transform: uppercase;
  }
  .person__role {
    font-size: 12px;
    text-transform: none;
    color: var(--silver-soft);
    border-left: 1px solid var(--silver-soft);
    padding-left: 5px;
    margin-left: 4px;
  }
  .contacts {
    position: absolute;
    top: 126px; left: 40px;
    list-style: none;
    font-size: 13px;
    line-height: 18px;
    color: var(--silver);
  }
  .contacts__label {
    display: inline-block;
    width: 14px;
    color: var(--red);
  }
  .contacts__plain { padding-left: 0; }
</style>
</head>
<body>
  <section class="card card--front" aria-label="Card front">
    <div class="brand-name"><span class="brand-mark"></span>Norvanta Kitchens</div>
    <div class="web">norvantakitchens.ca</div>
  </section>

  <section class="card card--back" aria-label="Card back">
    <div class="brand-name"><span class="brand-mark"></span>Norvanta Kitchens</div>
    <div class="person">Marcus Delvin<span class="person__role">Director</span></div>
    <ul class="contacts">
      <li><span class="contacts__label">P</span>555.210.4830</li>
      <li><span class="contacts__label">F</span>555.210.4831</li>
      <li><span class="contacts__label">C</span>555.384.2967</li>
      <li class="contacts__plain">marcus@norvantakitchens.ca</li>
      <li class="contacts__plain">1820 - 47 Ave., Northfield, AB T0X 4R2</li>
    </ul>
    <div class="web">norvantakitchens.ca</div>
  </section>
</body>
</html>
```